Business card design for engineering firm specializing in defense industry.

We need a professional business card design. Something simple but stands out. We are an engineering company specializing in composites in the defense industry.
Industry/Entity Type
Defense
Contact Information for Business Card
A simple black business card with the Varlonix yellow color is what we had in mind but open for other designs.
Colors
ffc214

```html
<!DOCTYPE html>
<html lang="en">
<head>
<meta charset="utf-8">
<title>Varlonix Business Card</title>
<link rel="stylesheet" href="https://fonts.googleapis.com/css2?family=Open+Sans:wght@400;700&display=swap">
<style>
  :root {
    --brand-yellow: #ffc214;
    --ink: #111111;
    --text-grey: #3a3a3a;
    --card-white: #ffffff;
    --backdrop: #2e2f31;
  }
  * { margin: 0; padding: 0; box-sizing: border-box; }
  html, body {
    width: 1200px; height: 1000px; overflow: hidden;
    background: var(--backdrop);
    font-family: "Open Sans", Arial, sans-serif;
  }
  .stage { position: relative; width: 1200px; height: 1000px; }
  .card {
    position: absolute; left: 250px; width: 700px; height: 400px;
    background: var(--card-white);
    overflow: hidden;
  }
  .card--back { top: 50px; }
  .card--front { top: 510px; }

  /* back side */
  .back-brand {
    position: absolute; left: 0; right: 0; top: 140px;
    display: flex; justify-content: center; align-items: center; gap: 16px;
  }
  .brand-square { width: 30px; height: 30px; background: var(--brand-yellow); }
  .back-brand .brand-name {
    font-weight: 700; font-size: 64px; color: var(--ink); letter-spacing: 1px;
  }
  .back-web {
    position: absolute; left: 0; right: 0; top: 250px; text-align: center;
    font-size: 18px; letter-spacing: 6px; color: var(--text-grey);
  }

  /* front side */
  .front-brand {
    position: absolute; left: 48px; top: 38px;
    font-weight: 700; font-size: 36px; color: var(--ink);
  }
  .contact {
    position: absolute; left: 48px; top: 125px;
    font-size: 16px; line-height: 21px; color: var(--text-grey);
    list-style: none;
  }
  .contact__address { padding-left: 24px; }
  .contact__row { display: flex; align-items: center; gap: 8px; }
  .contact__icon { width: 16px; height: 16px; flex: none; fill: var(--ink); }
  .name-panel {
    position: absolute; left: 380px; top: 195px; width: 200px; height: 115px;
    background: var(--brand-yellow);
    display: flex; flex-direction: column; justify-content: center; align-items: center;
  }
  .name-panel__name { font-weight: 700; font-size: 23px; color: var(--ink); line-height: 1.1; }
  .name-panel__title { font-size: 17px; color: var(--card-white); line-height: 1.3; }
</style>
</head>
<body>
<main class="stage">
  <section class="card card--back" aria-label="Business card back">
    <div class="back-brand">
      <span class="brand-square"></span>
      <span class="brand-name">Varlonix</span>
    </div>
    <p class="back-web">www.varlonix.com</p>
  </section>

  <section class="card card--front" aria-label="Business card front">
    <div class="front-brand">Varlonix</div>
    <ul class="contact">
      <li class="contact__address">4127 Harlow Ridge Road</li>
      <li class="contact__address">Brenton Falls, NY 12904</li>
      <li class="contact__row">
        <svg class="contact__icon" viewBox="0 0 16 16" aria-hidden="true"><path d="M1 5c0-2 3-3 7-3s7 1 7 3v2h-3V5.5H4V7H1z"/><rect x="3" y="8" width="10" height="6" rx="1"/></svg>
        <span>555 0142 7781</span>
      </li>
      <li class="contact__row">
        <svg class="contact__icon" viewBox="0 0 16 16" aria-hidden="true"><path d="M4 1h8v14H4zM5.5 2.5v9h5v-9z"/></svg>
        <span>555 0187 3394</span>
      </li>
      <li class="contact__row">
        <svg class="contact__icon" viewBox="0 0 16 16" aria-hidden="true"><rect x="4" y="1" width="8" height="5"/><rect x="1" y="6" width="14" height="7" rx="1"/><rect x="4" y="11" width="8" height="4"/></svg>
        <span>555 0163 2208</span>
      </li>
      <li class="contact__row">
        <svg class="contact__icon" viewBox="0 0 16 16" aria-hidden="true"><path d="M1 3h14v10H1z M1 3l7 6 7-6" stroke="#fff" stroke-width="1"/></svg>
        <span>daniel@varlonix.com</span>
      </li>
      <li class="contact__row">
        <svg class="contact__icon" viewBox="0 0 16 16" aria-hidden="true"><circle cx="8" cy="8" r="7"/><path d="M1 8h14M8 1c-3 3-3 11 0 14M8 1c3 3 3 11 0 14" stroke="#fff" stroke-width="1" fill="none"/></svg>
        <span>www.varlonix.com</span>
      </li>
    </ul>
    <div class="name-panel">
      <span class="name-panel__name">Daniel Marsh</span>
      <span class="name-panel__title">Founder</span>
    </div>
  </section>
</main>
</body>
</html>
```